Tidewind Coves Boat Business Website

I would like a website that looks fresh, fun and exciting with great colors and photos of people having fun sailing and power boating. Current web page is www.tidewindcoves.example. I want to be able to change content and photos myself once completed. Also needs to have customized info request forms and access to enrollment forms. Should work across all browsers and platforms including iPad and Mac. I have three product lines...instruction, charters and trips. See also keelhour.example/new-york, and facebook.com/tidewindcoves, /keelhournewyork and /coralpalmlounge.

Reason: We are reviewing the designs submitted and will provide feedback asap. Thank you.

Industry/Entity Type

Business

Requirements
Must have
• self management/content management
form submissions
color, fun, excitement
links pages
photo pages
Nice to have
• calendar/class scheduling
guest book
visitor uploadable photos

```html
<!DOCTYPE html>
<html lang="en">
<head>
<meta charset="utf-8">
<title>Tidewind Coves</title>
<link href="https://fonts.googleapis.com/css2?family=Open+Sans:ital,wght@0,400;0,600;0,700;1,400&family=Noto+Serif:wght@400;700&family=Montserrat:wght@500&display=swap" rel="stylesheet">
<style>
  :root {
    --ocean: #0a7fc2;
    --ocean-deep: #0a5a93;
    --teal: #17b3a3;
    --teal-dark: #138f94;
    --orange: #f7a21b;
    --orange-deep: #f08c00;
    --ink: #333333;
    --body: #555555;
    --line: #dcdcdc;
    --white: #ffffff;
  }
  * { box-sizing: border-box; margin: 0; padding: 0; }
  html, body { width: 1171px; height: 1200px; overflow: hidden; background: var(--white); }
  body { font-family: "Open Sans", Arial, sans-serif; color: var(--body); }
  .page { position: relative; width: 1171px; height: 1200px; }

  /* Header */
  .brand { position: absolute; left: 128px; top: 52px; font-family: "Noto Serif", Georgia, serif; font-size: 32px; font-weight: 400; color: var(--ocean-deep); line-height: 1; }

  .support { position: absolute; right: 106px; top: 14px; display: flex; align-items: center; gap: 8px; }
  .support-label { font-size: 11.5px; color: var(--ocean-deep); letter-spacing: 0.2px; }
  .support-phone { font-size: 19.5px; color: var(--ocean-deep); line-height: 1.05; }
  .social { position: absolute; right: 106px; top: 57px; display: flex; gap: 3px; }
  .social span { width: 21px; height: 20px; border-radius: 2px; }
  .social .s1 { background: #2d6fa3; } .social .s2 { background: #3bb0e3; }
  .social .s3 { background: #3b5b9a; } .social .s4 { background: #d8d8d8; }
  .upload { position: absolute; right: 106px; top: 85px; width: 186px; height: 38px; border-radius: 4px;
    background: linear-gradient(#0c6cae, #06487a); color: var(--white); display: flex; align-items: center; gap: 8px; padding-left: 10px; font-size: 14px; font-weight: 600; }

  /* Hero */
  .hero { position: absolute; left: 0; top: 133px; width: 1171px; height: 405px;
    background: linear-gradient(180deg, #8fa6bb 0%, #6f8fae 30%, #3f6994 55%, #8a6d4f 80%, #5a4632 100%); }
  .nav { position: absolute; left: 108px; top: 0; width: 957px; height: 44px; background: linear-gradient(#0b86c8, #0a5d98);
    display: flex; align-items: center; justify-content: space-between; padding: 0 12px 0 8px; font-size: 14px; color: var(--white); }
  .nav a { color: var(--white); text-decoration: none; }
  .nav .current { background: var(--white); color: var(--teal-dark); font-weight: 700; font-size: 12.5px; padding: 3px 8px; border-radius: 2px; letter-spacing: 0.5px; }
  .caption { position: absolute; left: 117px; top: 292px; font-family: "Montserrat", Arial, sans-serif; font-size: 25px; color: var(--white); }
  .caption span { display: block; width: 416px; white-space: nowrap; background: rgba(0,0,0,0.62); padding: 3px 8px 5px; margin-bottom: 2px; }
  .dots { position: absolute; right: 112px; top: 381px; display: flex; gap: 3px; }
  .dots i { width: 9px; height: 9px; border-radius: 50%; background: var(--white); }
  .dots i.on { background: var(--orange); }

  /* Product lines */
  .lines { position: absolute; top: 565px; left: 118px; width: 935px; height: 190px; }
  .line-card { position: absolute; top: 0; width: 284px; }
  .line-card:nth-child(1) { left: 0; } .line-card:nth-child(2) { left: 327px; } .line-card:nth-child(3) { left: 657px; }
  .line-head { display: flex; justify-content: space-between; align-items: flex-end; height: 42px; padding-bottom: 6px; border-bottom: 3px solid var(--ocean); }
  .line-head h3 { font-family: "Noto Serif", Georgia, serif; font-weight: 400; font-size: 19px; color: var(--ink); }
  .line-head h3::before { content: "→ "; font-family: "Open Sans", sans-serif; font-size: 14px; vertical-align: 4px; }
  .line-card p { margin-top: 18px; font-size: 12.2px; line-height: 19.5px; }
  .read { margin-top: 4px; font-size: 11px; font-weight: 600; letter-spacing: 0.4px; color: var(--teal); }
  .read::before { content: "→"; color: var(--ink); margin-right: 14px; font-weight: 400; }

  /* Newsletter */
  .newsletter { position: absolute; left: 115px; top: 783px; width: 938px; height: 49px; border-radius: 3px;
    background: linear-gradient(#0a86c8, #084f85); display: flex; align-items: center; padding: 0 11px 0 16px; }
  .newsletter h2 { font-weight: 400; font-size: 23px; color: var(--white); width: 255px; }
  .email { width: 528px; height: 33px; background: var(--white); border-radius: 2px; font-style: italic; font-size: 13px; color: var(--ink); display: flex; align-items: center; padding-left: 10px; }
  .signup { margin-left: 10px; width: 118px; height: 38px; border-radius: 3px; background: linear-gradient(#f5dc88, #e2b94e);
    font-family: "Noto Serif", Georgia, serif; font-size: 20px; color: #3a2e10; display: flex; align-items: center; justify-content: center; }

  /* Welcome */
  .welcome { position: absolute; left: 117px; top: 866px; width: 700px; }
  .welcome h1 { font-family: "Noto Serif", Georgia, serif; font-weight: 400; font-size: 28.5px; color: var(--ink); margin-bottom: 14px; }
  .welcome p { font-size: 12.2px; line-height: 22.5px; margin-bottom: 20px; }
  .more { position: absolute; left: 118px; top: 1084px; width: 137px; height: 38px; border-radius: 19px; background: var(--ocean);
    color: var(--white); font-size: 15px; display: flex; align-items: center; padding-left: 16px; }
  .more b { position: absolute; right: 5px; top: 5px; width: 28px; height: 28px; border-radius: 50%; background: var(--ocean-deep); border: 2px solid #4aa7de; }

  /* Calendar */
  .calendar { position: absolute; left: 815px; top: 883px; width: 226px; background: #f4f4f4; box-shadow: 0 4px 10px rgba(0,0,0,0.25); }
  .cal-head { height: 39px; background: linear-gradient(#ffb21e, var(--orange-deep)); color: var(--white); font-size: 16px; font-weight: 600;
    display: flex; align-items: center; justify-content: center; gap: 22px; }
  .cal-head i { font-style: normal; font-size: 10px; }
  .ring { position: absolute; top: -12px; width: 6px; height: 24px; border-radius: 3px; background: linear-gradient(90deg, #aaa, #fff, #999); }
  .cal-grid { display: grid; grid-template-columns: repeat(7, 1fr); }
  .cal-grid .dow { height: 18px; font-size: 8.5px; color: #777; text-align: center; line-height: 18px; border-bottom: 1px solid var(--line); }
  .cal-grid .d { position: relative; height: 32px; border-right: 1px solid var(--line); border-bottom: 1px solid var(--line); text-align: center; line-height: 28px; font-size: 13px; font-weight: 600; color: #555; }
  .cal-grid .d.off { color: #c8c8c8; font-weight: 400; }
  .cal-grid .d.today { background: var(--orange); color: var(--white); }
  .cal-grid .d.sel { background: #e2e2e2; }
  .cal-grid .d em { position: absolute; left: 50%; bottom: 5px; display: flex; gap: 2px; transform: translateX(-50%); }
  .cal-grid .d em i { width: 4px; height: 4px; border-radius: 50%; }
  .b { background: #3a8fd6; } .o { background: var(--orange); } .w { background: var(--white); }

  /* Footer */
  .footer { position: absolute; left: 0; top: 1148px; width: 1171px; height: 52px; background: linear-gradient(#3a3a3a, #262626);
    color: var(--white); font-size: 11.5px; display: flex; align-items: center; justify-content: space-between; padding: 0 97px 0 119px; }
</style>
</head>
<body>
<div class="page">
  <header>
    <div class="brand">Tidewind Coves</div>
    <div class="support">
      <svg width="40" height="38" viewBox="0 0 40 38" aria-hidden="true">
        <path d="M6 22 V16 a14 14 0 0 1 28 0 V22" fill="none" stroke="#222" stroke-width="3"/>
        <rect x="3" y="18" width="8" height="13" rx="3" fill="#222"/>
        <rect x="29" y="18" width="8" height="13" rx="3" fill="#222"/>
        <path d="M33 31 q0 5 -10 5" fill="none" stroke="#222" stroke-width="2"/>
      </svg>
      <div>
        <div class="support-label">24/7 SALES SUPPORT</div>
        <div class="support-phone">0800-555-0199</div>
      </div>
    </div>
    <div class="social"><span class="s1"></span><span class="s2"></span><span class="s3"></span><span class="s4"></span></div>
    <div class="upload">
      <svg width="26" height="24" viewBox="0 0 26 24" aria-hidden="true">
        <rect x="1" y="6" width="24" height="17" rx="2" fill="#fff"/>
        <path d="M13 2 L7 9 H11 V16 H15 V9 H19 Z" fill="#0a5d98" stroke="#fff" stroke-width="1"/>
      </svg>
      Upload Your Photos
    </div>
  </header>

  <section class="hero" role="img" aria-label="Photo of a smiling couple on the deck of a sailing yacht at sea in golden evening light">
    <nav class="nav">
      <a class="current" href="#">HOME</a>
      <a href="#">Nautical School</a>
      <a href="#">Charter Sailing</a>
      <a href="#">Charter Power</a>
      <a href="#">Our Captains</a>
      <a href="#">Adventure Travels</a>
      <a href="#">Sign Up Today</a>
      <a href="#">Contact Us</a>
    </nav>
    <div class="caption">
      <span>The World's Largest Fractional</span>
      <span>Boating Company</span>
    </div>
    <div class="dots"><i></i><i class="on"></i><i></i><i></i></div>
  </section>

  <section class="lines">
    <article class="line-card">
      <div class="line-head"><h3>Instruction</h3>
        <svg width="38" height="34" viewBox="0 0 38 34" aria-hidden="true">
          <path d="M4 4 L26 2 L30 22 L8 24 Z" fill="none" stroke="#27c0b0" stroke-width="3"/>
          <path d="M6 26 L32 24 L36 30 L10 32 Z" fill="#27c0b0"/>
        </svg></div>
      <p>Lorem ipsum dolor sit amet, consectetur adipiscing elit. Pellentesque quis nulla id orci malesuada porta posuere quis massa. Nunc vitae purus non augue scele risque ultricies vitae et velit.</p>
      <div class="read">READ</div>
    </article>
    <article class="line-card">
      <div class="line-head"><h3>Charters</h3>
        <svg width="38" height="38" viewBox="0 0 38 38" aria-hidden="true">
          <path d="M4 2 H22 L28 8 V14 M28 30 V34 H4 Z" fill="none" stroke="#0a5d98" stroke-width="3"/>
          <circle cx="20" cy="22" r="8" fill="none" stroke="#0a5d98" stroke-width="3.5"/>
          <path d="M26 28 L34 36" stroke="#0a5d98" stroke-width="4"/>
        </svg></div>
      <p>Lorem ipsum dolor sit amet, consectetur adipiscing elit. Pellentesque quis nulla id orci malesuada porta posuere quis massa. Nunc vitae purus non augue scele risque ultricies vitae et velit.</p>
      <div class="read">READ</div>
    </article>
    <article class="line-card">
      <div class="line-head"><h3>Trips</h3>
        <svg width="38" height="36" viewBox="0 0 38 36" aria-hidden="true">
          <circle cx="8" cy="9" r="5" fill="#27c0b0"/><circle cx="30" cy="9" r="5" fill="#27c0b0"/>
          <circle cx="19" cy="8" r="7" fill="#27c0b0"/>
          <path d="M1 26 q0-10 7-10 q7 0 7 10 Z M23 26 q0-10 7-10 q7 0 7 10 Z" fill="#27c0b0"/>
          <path d="M9 34 q0-16 10-16 q10 0 10 16 Z" fill="#27c0b0"/>
        </svg></div>
      <p>Lorem ipsum dolor sit amet, consectetur adipiscing elit. Pellentesque quis nulla id orci malesuada porta posuere quis massa. Nunc vitae purus non augue scele risque ultricies vitae et velit.</p>
      <div class="read">READ</div>
    </article>
  </section>

  <section class="newsletter">
    <h2>Newsletter Sign Up</h2>
    <div class="email">Enter your email address...</div>
    <div class="signup">Sign Up</div>
  </section>

  <section class="welcome">
    <h1>Welcome To Tidewind Coves</h1>
    <p>Lorem Ipsum is simply dummy text of the printing and typesetting industry. Lorem Ipsum has been the industry's standard dummy text ever since the 1500s, when an unknown printer took a galley of type and scrambled it to make a type specimen book. It has survived not only five centuries, but also the leap into electronic typesetting, remaining essentially unchanged.</p>
    <p>It was popularised in the 1960s with the release of Letraset sheets containing Lorem Ipsum passages, and more recently with desktop publishing software like Aldus PageMaker including versions of Lorem Ipsum.</p>
  </section>
  <div class="more">Read More
    <b><svg width="24" height="24" viewBox="0 0 24 24" aria-hidden="true"><path d="M7 7 L12 12 L7 17 M12 7 L17 12 L12 17" fill="none" stroke="#fff" stroke-width="2"/></svg></b>
  </div>

  <aside class="calendar">
    <span class="ring" style="left:18px"></span><span class="ring" style="right:18px"></span>
    <div class="cal-head"><i>◀</i>January 2013<i>▶</i></div>
    <div class="cal-grid">
      <div class="dow">SUN</div><div class="dow">MON</div><div class="dow">TUE</div><div class="dow">WED</div><div class="dow">THU</div><div class="dow">FRI</div><div class="dow">SAT</div>
      <div class="d off">30</div><div class="d">1<em><i class="b"></i></em></div><div class="d">2</div><div class="d">3</div><div class="d">4</div><div class="d">5<em><i class="o"></i></em></div><div class="d">7</div>
      <div class="d">8</div><div class="d">9</div><div class="d today">10<em><i class="w"></i></em></div><div class="d">11<em><i class="o"></i></em></div><div class="d">12</div><div class="d">13</div><div class="d">14</div>
      <div class="d">15</div><div class="d">16</div><div class="d">17</div><div class="d">18</div><div class="d">19</div><div class="d sel">20<em><i class="o"></i></em></div><div class="d">21</div>
      <div class="d">22<em><i class="b"></i></em></div><div class="d">23</div><div class="d">24</div><div class="d">25<em><i class="b"></i><i class="o"></i></em></div><div class="d">26</div><div class="d">27</div><div class="d">28</div>
      <div class="d">29</div><div class="d">30</div><div class="d">31</div><div class="d off">1</div><div class="d off">2</div><div class="d off">3</div><div class="d off">4</div>
    </div>
  </aside>

  <footer class="footer">
    <span>Copyright © 2013. All Rights Reserved</span>
    <span>Privacy policy &amp; Term of Uses</span>
  </footer>
</div>
</body>
</html>
```